New Manager Resource Guide & Planner

I need a template designed for a resource guide and planner that new managers would use to help guide them their first year managing others. Think your typical planner injected with tips, worksheets, quotes and other helpful tools. Initially, I'd like a template created for some key pages: one month, one week and single day layouts plus a quote page. I'm attaching a very rudimentary idea of the project, just need it purposefully designed with my colors and branding. The size is 6" x 8 " h. I would like this done in InDesign or Keynote so I can edit it and create other pages. Most likely, though, will contract you to finish out the entire project.

Target Market(s)

new managers (and HR directors who will most likely purchase the resource planner for their employees)

Industry/Entity Type

Advertising

Font styles to use
Other font styles liked:
• archer, open sans

Requirements
Must have
• a creative feel to it (I come from the advertising industry, so a fun design is OK). use of my branding and colors, be noticeably well designed.
Nice to have
• look at other planners for ideas. my goal is to use your template to build out the other pages I need. So think cool edging, or stylized quote boxes, etc.
Should not have
• please use the colors in my palette in the attached pdf plus any other complementary colors you see fit. my branding uses the font archer, open sans, use these and any other fonts that you see fit.

```html
<!DOCTYPE html>
<html lang="en">
<head>
<meta charset="utf-8">
<title>Daily Planner Page</title>
<link rel="stylesheet" href="https://fonts.googleapis.com/css2?family=Open+Sans:wght@400;700&family=Zilla+Slab:wght@400&family=Source+Code+Pro:wght@400&display=swap">
<style>
  :root {
    --lime: #d4e03e;
    --lime-text: #c6d236;
    --pale: #f8f9e4;
    --ink: #6d6e70;
    --accent: #f04e23;
    --paper: #ffffff;
  }
  html, body { margin: 0; padding: 0; width: 900px; height: 1200px; overflow: hidden; background: var(--paper); }
  .page { display: block; width: 900px; height: 1200px; }
  .section-title { font-family: "Open Sans", sans-serif; font-weight: 700; font-size: 17px; fill: var(--accent); }
  .task-num { font-family: "Zilla Slab", serif; font-size: 23px; fill: var(--ink); }
  .hint { font-family: "Open Sans", sans-serif; font-size: 12px; fill: var(--lime-text); }
  .col-head { font-family: "Open Sans", sans-serif; font-weight: 700; font-size: 12px; fill: var(--ink); }
  .slot-label { font-family: "Open Sans", sans-serif; font-size: 13px; fill: var(--ink); }
  .minor-num { font-family: "Source Code Pro", monospace; font-size: 11px; fill: var(--ink); }
  .brand-name { font-family: "Open Sans", sans-serif; font-weight: 700; font-size: 24px; letter-spacing: 1px; fill: var(--paper); }
  .outline { fill: none; stroke: var(--ink); stroke-width: 2; }
  .outline-lime { fill: var(--pale); stroke: var(--lime); stroke-width: 2; }
  .bracket { fill: none; stroke: var(--ink); stroke-width: 2; stroke-dasharray: 2 2; }
  .bracket-lime { fill: none; stroke: var(--lime); stroke-width: 2; stroke-dasharray: 2 2; }
  .task-line { fill: none; stroke: var(--ink); stroke-width: 1.6; }
  .colon-lime { fill: var(--lime); }
  .colon-ink { fill: var(--ink); }
  .icon { fill: none; stroke: #9a9b9d; stroke-width: 1.6; }
  .icon-num { font-family: "Open Sans", sans-serif; font-size: 9px; fill: #9a9b9d; text-anchor: middle; }
  .dot-row-lime { stroke: var(--lime); stroke-width: 2.4; stroke-linecap: round; stroke-dasharray: 0 14.55; }
</style>
</head>
<body>
<svg class="page" viewBox="0 0 1000 1333" xmlns="http://www.w3.org/2000/svg">
  <defs>
    <pattern id="quarter-box" x="115" y="132" width="30" height="29.35" patternUnits="userSpaceOnUse">
      <rect x="1" y="1" width="26" height="26.5" rx="6" fill="#fff" stroke="#6d6e70" stroke-width="2"/>
    </pattern>
    <pattern id="quarter-box-lime" x="115" y="132" width="30" height="29.35" patternUnits="userSpaceOnUse">
      <rect x="1" y="1" width="26" height="26.5" rx="6" fill="#f8f9e4" stroke="#d4e03e" stroke-width="2"/>
    </pattern>
    <pattern id="dot-row" x="148" y="116.33" width="14.55" height="29.35" patternUnits="userSpaceOnUse">
      <circle cx="1.5" cy="14.67" r="1.2" fill="#6d6e70"/>
    </pattern>
    <pattern id="dot-row-lime" x="148" y="116.33" width="14.55" height="29.35" patternUnits="userSpaceOnUse">
      <circle cx="1.5" cy="14.67" r="1.3" fill="#d4e03e"/>
    </pattern>
    <pattern id="minor-dots" x="515" y="743.7" width="22.2" height="28.6" patternUnits="userSpaceOnUse">
      <circle cx="1.5" cy="14.3" r="1.2" fill="#6d6e70"/>
    </pattern>
  </defs>

  <g class="header">
    <rect x="0" y="0" width="1000" height="15" fill="var(--lime)"/>
    <rect x="0" y="74" width="1000" height="2.5" fill="var(--lime)"/>
    <g class="water-glasses">
      <path class="icon" d="M523 40 h18 l-2 23 h-14 z"/><text class="icon-num" x="532" y="57">1</text>
      <path class="icon" d="M555 40 h18 l-2 23 h-14 z"/><text class="icon-num" x="564" y="57">2</text>
      <path class="icon" d="M587 40 h18 l-2 23 h-14 z"/><text class="icon-num" x="596" y="57">3</text>
      <path class="icon" d="M619 40 h18 l-2 23 h-14 z"/><text class="icon-num" x="628" y="57">4</text>
      <path class="icon" d="M651 40 h18 l-2 23 h-14 z"/><text class="icon-num" x="660" y="57">5</text>
      <path class="icon" d="M683 40 h18 l-2 23 h-14 z"/><text class="icon-num" x="692" y="57">6</text>
    </g>
    <rect x="735" y="30" width="2" height="38" fill="#e2e2e2"/>
    <g class="coffee-cups">
      <path class="icon" d="M774 48 h18 l-2 13 h-14 z M791 51 a4 4 0 0 1 0 8"/><text class="icon-num" x="783" y="59">1</text>
      <path class="icon" d="M806 48 h18 l-2 13 h-14 z M823 51 a4 4 0 0 1 0 8"/><text class="icon-num" x="815" y="59">2</text>
      <path class="icon" d="M838 48 h18 l-2 13 h-14 z M855 51 a4 4 0 0 1 0 8"/><text class="icon-num" x="847" y="59">3</text>
      <path class="icon" d="M870 48 h18 l-2 13 h-14 z M887 51 a4 4 0 0 1 0 8"/><text class="icon-num" x="879" y="59">4</text>
      <path class="icon" d="M902 48 h18 l-2 13 h-14 z M919 51 a4 4 0 0 1 0 8"/><text class="icon-num" x="911" y="59">5</text>
      <path class="icon" d="M934 48 h18 l-2 13 h-14 z M951 51 a4 4 0 0 1 0 8"/><text class="icon-num" x="943" y="59">6</text>
    </g>
  </g>

  <g class="schedule">
    <g class="hour-markers">
      <path class="bracket" d="M33 114 v14 h42 v-14"/><text class="slot-label" x="54" y="143" text-anchor="middle">start</text>
      <path class="bracket" d="M33 232 v14 h42 v-14"/>
      <path class="bracket" d="M33 349 v14 h42 v-14"/>
      <path class="bracket" d="M33 467 v14 h42 v-14"/>
      <path class="bracket-lime" d="M33 584 v14 h42 v-14"/>
      <text class="slot-label" x="54" y="617" text-anchor="middle">mid</text>
      <text class="slot-label" x="54" y="633" text-anchor="middle">break</text>
      <path class="bracket" d="M33 702 v14 h42 v-14"/>
      <path class="bracket" d="M33 819 v14 h42 v-14"/>
      <path class="bracket" d="M33 937 v14 h42 v-14"/>
      <path class="bracket" d="M33 1054 v14 h42 v-14"/>
      <text class="slot-label" x="55" y="1187" text-anchor="middle">review</text>
      <path class="bracket-lime" d="M34 1195 h42"/>
    </g>

    <g class="hour-column">
      <rect class="outline" x="87" y="105" width="25" height="465" rx="7"/>
      <rect x="86" y="217" width="27" height="5" fill="#fff"/><path class="bracket" d="M89 217 h21 M89 222 h21"/>
      <rect x="86" y="334" width="27" height="5" fill="#fff"/><path class="bracket" d="M89 334 h21 M89 339 h21"/>
      <rect x="86" y="452" width="27" height="5" fill="#fff"/><path class="bracket" d="M89 452 h21 M89 457 h21"/>
      <text class="col-head" x="99.5" y="123" text-anchor="middle">60</text>
      <rect class="outline-lime" x="87" y="575" width="25" height="113" rx="7"/>
      <rect class="outline" x="87" y="693" width="25" height="465" rx="7"/>
      <rect x="86" y="804" width="27" height="5" fill="#fff"/><path class="bracket" d="M89 804 h21 M89 809 h21"/>
      <rect x="86" y="922" width="27" height="5" fill="#fff"/><path class="bracket" d="M89 922 h21 M89 927 h21"/>
      <rect x="86" y="1039" width="27" height="5" fill="#fff"/><path class="bracket" d="M89 1039 h21 M89 1044 h21"/>
      <rect class="outline-lime" x="87" y="1201" width="25" height="55" rx="7"/>
    </g>

    <g class="quarter-column">
      <rect class="outline" x="116" y="105" width="26" height="25" rx="6"/>
      <text class="col-head" x="129" y="123" text-anchor="middle">15</text>
      <rect x="115" y="132" width="30" height="440.25" fill="url(#quarter-box)"/>
      <rect x="115" y="572.25" width="30" height="117.4" fill="url(#quarter-box-lime)"/>
      <rect x="115" y="689.65" width="30" height="469.6" fill="url(#quarter-box)"/>
      <rect class="outline-lime" x="116" y="1201" width="26" height="26" rx="6"/>
      <rect class="outline-lime" x="116" y="1230" width="26" height="26" rx="6"/>
    </g>

    <g class="note-lines">
      <rect x="146" y="120" width="332" height="442" fill="url(#dot-row)"/>
      <rect x="146" y="562" width="332" height="140" fill="url(#dot-row-lime)"/>
      <rect x="146" y="702" width="332" height="465" fill="url(#dot-row)"/>
      <line class="dot-row-lime" x1="148" y1="1198" x2="476" y2="1198"/>
      <line class="dot-row-lime" x1="148" y1="1228" x2="476" y2="1228"/>
      <line class="dot-row-lime" x1="148" y1="1257" x2="476" y2="1257"/>
    </g>
  </g>

  <g class="major-tasks">
    <path d="M493 110 h14 l-7 12 z" fill="var(--ink)"/>
    <text class="section-title" x="534" y="123">MAJOR TASKS</text>
    <g class="task-row">
      <text class="task-num" x="503" y="178">01</text>
      <path class="task-line" d="M536 156 v23 h422 v-4"/>
      <rect class="colon-lime" x="561" y="171" width="2" height="2"/><rect class="colon-lime" x="561" y="176" width="2" height="2"/>
      <rect class="colon-lime" x="587" y="171" width="2" height="2"/><rect class="colon-lime" x="587" y="176" width="2" height="2"/>
      <rect class="colon-ink" x="910" y="171" width="2" height="2"/><rect class="colon-ink" x="910" y="176" width="2" height="2"/>
      <text class="hint" x="557" y="196">Task description. Indent for subtasks.</text>
      <text class="hint" x="965" y="196" text-anchor="end">Total time.</text>
    </g>
    <g class="task-row">
      <text class="task-num" x="503" y="232">02</text>
      <path class="task-line" d="M536 209 v23 h422 v-4"/>
      <rect class="colon-lime" x="561" y="224" width="2" height="2"/><rect class="colon-lime" x="561" y="229" width="2" height="2"/>
      <rect class="colon-lime" x="587" y="224" width="2" height="2"/><rect class="colon-lime" x="587" y="229" width="2" height="2"/>
      <rect class="colon-ink" x="910" y="224" width="2" height="2"/><rect class="colon-ink" x="910" y="229" width="2" height="2"/>
    </g>
    <g class="task-row">
      <text class="task-num" x="503" y="284">03</text>
      <path class="task-line" d="M536 262 v23 h422 v-4"/>
      <rect class="colon-lime" x="561" y="277" width="2" height="2"/><rect class="colon-lime" x="561" y="282" width="2" height="2"/>
      <rect class="colon-lime" x="587" y="277" width="2" height="2"/><rect class="colon-lime" x="587" y="282" width="2" height="2"/>
      <rect class="colon-ink" x="910" y="277" width="2" height="2"/><rect class="colon-ink" x="910" y="282" width="2" height="2"/>
    </g>
    <g class="task-row">
      <text class="task-num" x="503" y="362">04</text>
      <path class="task-line" d="M536 340 v23 h422 v-4"/>
      <rect class="colon-lime" x="561" y="355" width="2" height="2"/><rect class="colon-lime" x="561" y="360" width="2" height="2"/>
      <rect class="colon-lime" x="587" y="355" width="2" height="2"/><rect class="colon-lime" x="587" y="360" width="2" height="2"/>
      <rect class="colon-ink" x="910" y="355" width="2" height="2"/><rect class="colon-ink" x="910" y="360" width="2" height="2"/>
    </g>
    <g class="task-row">
      <text class="task-num" x="503" y="416">05</text>
      <path class="task-line" d="M536 394 v23 h422 v-4"/>
      <rect class="colon-lime" x="561" y="409" width="2" height="2"/><rect class="colon-lime" x="561" y="414" width="2" height="2"/>
      <rect class="colon-lime" x="587" y="409" width="2" height="2"/><rect class="colon-lime" x="587" y="414" width="2" height="2"/>
      <rect class="colon-ink" x="910" y="409" width="2" height="2"/><rect class="colon-ink" x="910" y="414" width="2" height="2"/>
    </g>
    <g class="task-row">
      <text class="task-num" x="503" y="467">06</text>
      <path class="task-line" d="M536 447 v23 h422 v-4"/>
      <rect class="colon-lime" x="561" y="462" width="2" height="2"/><rect class="colon-lime" x="561" y="467" width="2" height="2"/>
      <rect class="colon-lime" x="587" y="462" width="2" height="2"/><rect class="colon-lime" x="587" y="467" width="2" height="2"/>
      <rect class="colon-ink" x="910" y="462" width="2" height="2"/><rect class="colon-ink" x="910" y="467" width="2" height="2"/>
    </g>
    <g class="task-row">
      <text class="task-num" x="503" y="547">07</text>
      <path class="task-line" d="M536 527 v23 h422 v-4"/>
      <rect class="colon-lime" x="561" y="542" width="2" height="2"/><rect class="colon-lime" x="561" y="547" width="2" height="2"/>
      <rect class="colon-lime" x="587" y="542" width="2" height="2"/><rect class="colon-lime" x="587" y="547" width="2" height="2"/>
      <rect class="colon-ink" x="910" y="542" width="2" height="2"/><rect class="colon-ink" x="910" y="547" width="2" height="2"/>
    </g>
    <g class="task-row">
      <text class="task-num" x="503" y="601">08</text>
      <path class="task-line" d="M536 581 v23 h422 v-4"/>
      <rect class="colon-lime" x="561" y="596" width="2" height="2"/><rect class="colon-lime" x="561" y="601" width="2" height="2"/>
      <rect class="colon-lime" x="587" y="596" width="2" height="2"/><rect class="colon-lime" x="587" y="601" width="2" height="2"/>
      <rect class="colon-ink" x="910" y="596" width="2" height="2"/><rect class="colon-ink" x="910" y="601" width="2" height="2"/>
    </g>
    <g class="task-row">
      <text class="task-num" x="503" y="653">09</text>
      <path class="task-line" d="M536 634 v23 h422 v-4"/>
      <rect class="colon-lime" x="561" y="649" width="2" height="2"/><rect class="colon-lime" x="561" y="654" width="2" height="2"/>
      <rect class="colon-lime" x="587" y="649" width="2" height="2"/><rect class="colon-lime" x="587" y="654" width="2" height="2"/>
      <rect class="colon-ink" x="910" y="649" width="2" height="2"/><rect class="colon-ink" x="910" y="654" width="2" height="2"/>
    </g>
  </g>

  <g class="minor-tasks">
    <path d="M493 693 h14 l-7 12 z" fill="var(--ink)"/>
    <text class="section-title" x="530" y="707">MINOR TASKS</text>
    <text class="minor-num" x="510" y="748">10</text>
    <text class="minor-num" x="510" y="777">11</text>
    <text class="minor-num" x="510" y="805">12</text>
    <text class="minor-num" x="510" y="834">13</text>
    <text class="minor-num" x="510" y="862">14</text>
    <text class="minor-num" x="510" y="891">15</text>
    <text class="minor-num" x="510" y="920">16</text>
    <text class="minor-num" x="510" y="948">17</text>
    <text class="minor-num" x="510" y="977">18</text>
    <text class="minor-num" x="510" y="1005">19</text>
    <text class="minor-num" x="510" y="1034">20</text>
    <rect x="513" y="745" width="450" height="305" fill="url(#minor-dots)"/>
  </g>

  <rect class="notes-box" x="517" y="1062" width="443" height="214" fill="var(--pale)"/>

  <g class="footer">
    <rect x="0" y="1285" width="1000" height="48" fill="var(--lime)"/>
    <circle cx="800" cy="1309" r="7" fill="var(--paper)"/>
    <text class="brand-name" x="960" y="1318" text-anchor="end">Lumen Leaders</text>
  </g>
</svg>
</body>
</html>
```